New business card design needed for Diesel Fitting (Mechanical) Company

We need a new business card for our company called "Granite Valley Engineering" that showcases our logo and business details.
Target Market(s)
Owners of all makes and models of vehicles, trucks, plant and machinery.
Industry/Entity Type
Mechanical
Contact Information for Business Card
The business card details need to include the following: Owners/Directors: Trevor & Marisol Dunn-Calloway ABN: 47 913 206 781 Address: 561 Beaumont Street CHARTERS TOWERS QLD 4820 Postal Address: PO Box 8716 CHARTERS TOWERS QLD 4820 Website: www.gvengineering.com.au Phone: 4732 9185 Mobile: 0491 375 806 Emails: sales@gvengineering.com.au; admin@gvengineering.com.au; accounts@gvengineering.com.au; parts@gvengineering.com.au; office@gvengineering.com.au, reception@gvengineering.com.au
Look and feel

```html
<!DOCTYPE html>
<html lang="en">
<head>
<meta charset="utf-8">
<title>Granite Valley Engineering – Business Card</title>
<link rel="stylesheet" href="https://fonts.googleapis.com/css2?family=Questrial&family=Montserrat:wght@700&display=swap">
<style>
  :root {
    --page: #1c1c1c;
    --card-white: #ffffff;
    --card-black: #0d0d0d;
    --card-black-2: #202020;
    --orange: #f07a22;
    --red: #e32127;
    --grey: #8c8c8c;
    --ink: #1a1a1a;
    --light: #f2f2f2;
  }
  * { box-sizing: border-box; margin: 0; padding: 0; }
  html, body { width: 1200px; height: 1200px; overflow: hidden; }
  body {
    background: var(--page);
    font-family: "Questrial", "Century Gothic", sans-serif;
    position: relative;
  }

  /* ---------- Front card ---------- */
  .card-front {
    position: absolute; left: 50px; top: 400px;
    width: 700px; height: 400px;
    background: var(--card-white);
    border-radius: 22px;
    overflow: hidden;
    color: var(--ink);
    box-shadow: 0 20px 40px rgba(0,0,0,.5);
  }
  .card-front .base-band {
    position: absolute; left: 0; right: 0; bottom: 0; height: 9px;
    background: var(--red);
  }
  .brand {
    position: absolute; left: 34px; top: 46px;
    display: flex; align-items: center; gap: 12px;
  }
  .brand-dot {
    width: 30px; height: 30px; border-radius: 50%;
    background: var(--orange);
  }
  .brand-name {
    font-size: 27px; color: var(--orange); line-height: 1;
  }
  .abn {
    position: absolute; left: 541px; top: 122px;
    font-size: 13px; line-height: 16px; padding-bottom: 3px;
    border-bottom: 2px solid var(--grey);
    white-space: nowrap;
  }
  .divider {
    position: absolute; left: 368px; top: 136px;
    width: 175px; height: 60px;
  }
  .owners {
    position: absolute; left: 34px; top: 176px;
  }
  .owners .names {
    font-size: 17px; line-height: 20px; letter-spacing: -.2px; white-space: nowrap;
  }
  .owners .names strong {
    font-family: "Montserrat", sans-serif; font-weight: 700; color: var(--red);
  }
  .owners .names span { color: #444; }
  .owners .role { font-size: 13px; margin-top: 4px; }
  .contact {
    position: absolute; font-size: 13px; line-height: 1.35;
  }
  .contact-row { display: flex; align-items: flex-start; gap: 7px; }
  .contact-row svg { flex: none; margin-top: 2px; }
  .contact-postal { right: 40px; top: 238px; }
  .contact-street { left: 34px; top: 316px; }
  .web strong { color: var(--red); font-weight: 400; }

  /* ---------- Back card ---------- */
  .card-back {
    position: absolute; left: 800px; top: 300px;
    width: 350px; height: 600px;
    background: linear-gradient(160deg, var(--card-black-2) 0%, var(--card-black) 55%, #141414 100%);
    border-radius: 22px;
    overflow: hidden;
    color: var(--light);
    box-shadow: 0 20px 40px rgba(0,0,0,.6);
  }
  .back-brand {
    position: absolute; left: 0; right: 0; top: 60px;
    display: flex; flex-direction: column; align-items: center; gap: 14px;
  }
  .back-brand .brand-dot { width: 44px; height: 44px; }
  .back-brand .brand-name { font-size: 24px; text-align: center; }
  .email-list {
    position: absolute; left: 50px; top: 210px;
    list-style: none;
  }
  .email-list li {
    font-size: 15px; padding: 7px 0 9px;
    position: relative;
  }
  .email-list li::after {
    content: ""; position: absolute; left: 30px; bottom: 0;
    width: 180px; height: 1px;
    background: linear-gradient(90deg, transparent, var(--red) 50%, transparent);
  }
  .back-rule {
    position: absolute; left: 60px; top: 500px;
    width: 230px; height: 40px;
  }
</style>
</head>
<body>

<section class="card-front" aria-label="Business card front">
  <div class="brand">
    <span class="brand-dot"></span>
    <span class="brand-name">Granite Valley Engineering</span>
  </div>

  <div class="abn">ABN: 47 913 206 781</div>

  <svg class="divider" viewBox="0 0 175 60" aria-hidden="true">
    <polyline points="0,50 150,50 156,38 161,56 169,7 175,7" fill="none" stroke="#8c8c8c" stroke-width="2"/>
  </svg>

  <div class="owners">
    <p class="names"><strong>TREVOR &amp; MARISOL</strong> <span>DUNN-CALLOWAY</span></p>
    <p class="role">Owners/Directors</p>
  </div>

  <div class="contact contact-postal">
    <div class="contact-row">
      <svg width="11" height="14" viewBox="0 0 12 16"><path d="M6 0a6 6 0 0 0-6 6c0 4.5 6 10 6 10s6-5.5 6-10a6 6 0 0 0-6-6zm0 8.5A2.5 2.5 0 1 1 6 3.5a2.5 2.5 0 0 1 0 5z" fill="#f07a22"/></svg>
      <p>PO Box 8716 Charters Towers<br>QLD 4820</p>
    </div>
    <div class="contact-row web">
      <svg width="12" height="12" viewBox="0 0 12 12"><circle cx="6" cy="6" r="5.2" fill="none" stroke="#f07a22" stroke-width="1.2"/><path d="M1 6h10M6 1c-2.5 3-2.5 7 0 10M6 1c2.5 3 2.5 7 0 10" fill="none" stroke="#f07a22" stroke-width="1"/></svg>
      <p>www.<strong>gvengineering</strong>.com.au</p>
    </div>
  </div>

  <div class="contact contact-street">
    <div class="contact-row">
      <svg width="11" height="14" viewBox="0 0 12 16"><path d="M6 0a6 6 0 0 0-6 6c0 4.5 6 10 6 10s6-5.5 6-10a6 6 0 0 0-6-6zm0 8.5A2.5 2.5 0 1 1 6 3.5a2.5 2.5 0 0 1 0 5z" fill="#f07a22"/></svg>
      <p>561 Beaumont Street,<br>Charters Towers QLD 4820</p>
    </div>
    <div class="contact-row">
      <svg width="12" height="12" viewBox="0 0 12 12"><path d="M2.5 1l2 2.5-1.2 1.3a7 7 0 0 0 3.9 3.9L8.5 7.5 11 9.5 9.8 11C5 11 1 7 1 2.2z" fill="#f07a22"/></svg>
      <p>4732 9185 | <svg width="8" height="12" viewBox="0 0 8 12" style="vertical-align:-1px"><rect x=".6" y=".6" width="6.8" height="10.8" rx="1.2" fill="none" stroke="#f07a22" stroke-width="1.2"/></svg> 0491 375 806</p>
    </div>
  </div>

  <div class="base-band"></div>
</section>

<section class="card-back" aria-label="Business card back">
  <div class="back-brand">
    <span class="brand-dot"></span>
    <span class="brand-name">Granite Valley Engineering</span>
  </div>

  <ul class="email-list">
    <li>sales@gvengineering.com.au</li>
    <li>admin@gvengineering.com.au</li>
    <li>accounts@gvengineering.com.au</li>
    <li>parts@gvengineering.com.au</li>
    <li>office@gvengineering.com.au</li>
    <li>reception@gvengineering.com.au</li>
  </ul>

  <svg class="back-rule" viewBox="0 0 230 40" aria-hidden="true">
    <polyline points="0,20 100,20 108,8 113,32 120,4 130,20 230,20" fill="none" stroke="#8c8c8c" stroke-width="2"/>
  </svg>
</section>

</body>
</html>
```